Option Sheet

We need a one page option sheet with a left to right reading of the five options. It should be a one sheet, multiple colors and definitive separations between options This is used in a sales consultation. Backround or colors not in option need to have the follow RGB value (5 red, 20 green, 63 blue)

We added a smaller text file, please change that point

Target Market(s)

Divorce

Industry/Entity Type

Legal

Requirements
Must have
• 1) All five options left to right
• 2)language included in sheet

```html
<!DOCTYPE html>
<html lang="en">
<head>
<meta charset="utf-8">
<title>Five Options – Divorce</title>
<link href="https://fonts.googleapis.com/css2?family=Open+Sans:wght@400;600;700;800&family=Oswald:wght@600;700&display=swap" rel="stylesheet">
<style>
  :root {
    --navy: rgb(5, 20, 63);
    --gold-line: #b48a5c;
    --bronze: #b48c60;
    --bronze-dark: #8e6a45;
    --ink: #1b2550;
    --white: #ffffff;
    --band-blue: #3d4fb3;
    --band-blue-light: #5567c9;
    --band-red: #bf2430;
    --band-red-light: #d43a43;
    --pink-a: #ee4f97;
    --pink-b: #f88ac0;
    --blue-a: #4f7fe0;
    --blue-b: #8fb4f5;
    --orange-a: #f6931f;
    --orange-b: #fcc56e;
    --green-a: #7dbb55;
    --green-b: #b5dd8f;
    --yellow-a: #fcc300;
    --yellow-b: #fde46a;
  }
  * { box-sizing: border-box; margin: 0; padding: 0; }
  html, body { width: 1200px; height: 889px; overflow: hidden; background: var(--navy); }
  .sheet {
    position: relative; width: 1200px; height: 889px;
    background: var(--navy);
    font-family: "Open Sans", Arial, sans-serif;
    color: var(--ink);
  }
  .rule { position: absolute; height: 5px; background: var(--gold-line); }
  .rule--top-left { left: 54px; top: 27px; width: 356px; }
  .rule--top-right { left: 796px; top: 27px; width: 357px; }
  .rule--bottom { left: 54px; top: 868px; width: 1099px; }

  .heading {
    position: absolute; left: 0; top: 16px; width: 1200px; text-align: center;
    color: var(--white); font-weight: 800; font-size: 29px; letter-spacing: 0.5px;
  }
  .figure {
    position: absolute; left: 322px; top: 58px; width: 118px; height: 90px;
    background: linear-gradient(180deg, #c9ccd4, #8d93a3);
    border-radius: 40px 40px 10px 30px;
    opacity: 0.9;
  }
  .wordmark {
    position: absolute; left: 418px; top: 46px; width: 370px;
    font-family: "Oswald", "Arial Narrow", sans-serif; font-weight: 700;
    font-size: 96px; line-height: 1; letter-spacing: 3px;
    color: var(--bronze);
  }

  .option { position: absolute; top: 188px; width: 206px; }
  .option__bg {
    position: absolute; inset: 0;
    clip-path: polygon(0 31px, 50% 0, 100% 31px, 100% 100%, 0 100%);
  }
  .option--pink .option__bg { background: linear-gradient(90deg, var(--pink-a), var(--pink-b)); }
  .option--blue .option__bg { background: linear-gradient(90deg, var(--blue-a), var(--blue-b)); }
  .option--orange .option__bg { background: linear-gradient(90deg, var(--orange-a), var(--orange-b)); }
  .option--green .option__bg { background: linear-gradient(90deg, var(--green-a), var(--green-b)); }
  .option--yellow .option__bg { background: linear-gradient(90deg, var(--yellow-a), var(--yellow-b)); }

  .option__inner { position: relative; padding-bottom: 14px; }
  .option__number {
    display: block; width: 28px; height: 28px; margin: 10px auto 0;
    border: 2px solid var(--ink); border-radius: 50%;
    text-align: center; font-size: 18px; font-weight: 600; line-height: 24px;
  }
  .option__title {
    height: 66px; padding-top: 2px; text-align: center;
    font-size: 19px; font-weight: 800; line-height: 21px; text-transform: uppercase;
  }
  .band {
    margin: 0 -3px; height: 30px; line-height: 30px; text-align: center;
    color: var(--white); font-weight: 800; font-size: 18px; text-transform: uppercase;
  }
  .band--pro { background: linear-gradient(90deg, var(--band-blue), var(--band-blue-light)); }
  .band--con { background: linear-gradient(90deg, var(--band-red), var(--band-red-light)); }

  .points { list-style: none; padding: 14px 10px 10px 8px; }
  .points li {
    position: relative; padding-left: 26px; margin-bottom: 12px;
    font-size: 15.5px; font-weight: 600; line-height: 18px;
  }
  .points li:last-child { margin-bottom: 4px; }
  .points li::before {
    content: ""; position: absolute; left: 0; top: 1px; width: 16px; height: 16px;
    background: var(--white); border: 2px solid var(--ink);
  }
  .points li::after {
    content: ""; position: absolute; left: 5px; top: 2px; width: 6px; height: 11px;
    border: solid var(--ink); border-width: 0 3px 3px 0; transform: rotate(40deg);
  }
</style>
</head>
<body>
<div class="sheet">
  <div class="rule rule--top-left"></div>
  <div class="rule rule--top-right"></div>
  <div class="rule rule--bottom"></div>

  <h1 class="heading">FIVE OPTIONS</h1>
  <div class="figure" role="img" aria-label="Silhouette of a person sitting with head resting on knees"></div>
  <div class="wordmark">DIVORCE</div>

  <section class="option option--pink" style="left:54px; height:443px;">
    <div class="option__bg"></div>
    <div class="option__inner">
      <span class="option__number">1</span>
      <h2 class="option__title">Do<br>Nothing</h2>
      <div class="band band--pro">Advantages</div>
      <ul class="points">
        <li>Stay married</li>
        <li>No life Changes</li>
      </ul>
      <div class="band band--con">Disadvantages</div>
      <ul class="points">
        <li>Remain unhappy, depressed, anxious</li>
        <li>Money and assets may disappear</li>
        <li>What is going to change?</li>
      </ul>
    </div>
  </section>

  <section class="option option--blue" style="left:276px; height:560px;">
    <div class="option__bg"></div>
    <div class="option__inner">
      <span class="option__number">2</span>
      <h2 class="option__title">Go to<br>Counceling</h2>
      <div class="band band--pro">Advantages</div>
      <ul class="points">
        <li>Reconcile marriage</li>
        <li>Help make a better life</li>
      </ul>
      <div class="band band--con">Disadvantages</div>
      <ul class="points">
        <li>Past issues are highlighted and may drudge up old wounds</li>
        <li>It may just clarify the reasons you need to separate and/or divorce</li>
        <li>Both parties must be invested and willing to participate</li>
      </ul>
    </div>
  </section>

  <section class="option option--orange" style="left:498px; height:596px;">
    <div class="option__bg"></div>
    <div class="option__inner">
      <span class="option__number">3</span>
      <h2 class="option__title">Do it<br>Yourself</h2>
      <div class="band band--pro">Advantages</div>
      <ul class="points">
        <li>No attorney fees</li>
        <li>You are your on attorney</li>
      </ul>
      <div class="band band--con">Disadvantages</div>
      <ul class="points">
        <li>People often find that what is “fair,” may in fact, not be truly fair</li>
        <li>Often times, people do not know the risks</li>
        <li>Complicated legal system within intrigue rules</li>
        <li>Unsure how to com-plete the necessary paperwork and meet the deadlines</li>
      </ul>
    </div>
  </section>

  <section class="option option--green" style="left:721px; height:662px;">
    <div class="option__bg"></div>
    <div class="option__inner">
      <span class="option__number">4</span>
      <h2 class="option__title">Limited<br>Representation</h2>
      <div class="band band--pro">Advantages</div>
      <ul class="points">
        <li>Balance between going alone and our limited involvement in the case</li>
      </ul>
      <div class="band band--con">Disadvantages</div>
      <ul class="points">
        <li>Our terms may not benefit from our legal knowledge</li>
        <li>The legal conse-quences of your legal documents will not be explained to you so that you can formulate a plan for handling the rest of your case.</li>
        <li>Your spouse or other parties may cause your legal fees to increase significantly without action on your part</li>
      </ul>
    </div>
  </section>

  <section class="option option--yellow" style="left:946px; height:491px;">
    <div class="option__bg"></div>
    <div class="option__inner">
      <span class="option__number">5</span>
      <h2 class="option__title">Hire<br>Us</h2>
      <div class="band band--pro">Advantages</div>
      <ul class="points">
        <li>Gain the full benefits of our experience</li>
        <li>Have a team of Family Law focus attorneys</li>
        <li>Often saves you or makes you money in the long run</li>
        <li>Save you time, energy and stress</li>
      </ul>
      <div class="band band--con">Disadvantages</div>
      <ul class="points">
        <li>Initial cost</li>
      </ul>
    </div>
  </section>
</div>
</body>
</html>
```